依頼概要
■依頼目的/概要
Tolino(ブログ)内で「診断レポート」を提供しますので、
表紙デザイン作成をお願いいたします。

■納品物
下記での納品をお願いいたします。
JPEG形式
横1600ピクセル×縦2560ピクセル

■診断レポートの内容
<レポートのタイトル>
40代からのあなたの強みを最大限に生かすための3つの視点 ビジネスもプライベートも充実した人生を手に入れる

<キャッチコピー>
以下の文言の中から組み合わせるか、選んで載せてください。

・他人軸で生きる辛さから脱却しないと人生に悔いが残る!

・人生の転機のヒントが得られる!

・自分らしく生きるヒントが分かる!

・ハンディや持病を抱えながらも一部上場企業に貢献し、独立・起業したコーチが伝える

<著者名>
・著者名 前田芳典(ライフコーチ) M&R 合同会社 代表

■デザイン要望
・本のタイトル/キャッチコピー/著者名の反映をお願い致します。

・読者は40代50代60代の自分らしく生きようとしている人です。

・これからの人生設計を踏まえた考え方や捉え方を書いたレポートですので、
「ビジネス書の表紙」というイメージでお願いします。

・タイトル文字数が、ちょっと多いのですが、
できるだけ文字を認識しやすいようにしたいです。

・未来の人生に新たな可能性が見えるイメージです。

・タイトルの中では、「強み」「充実した人生」「生かす」
あたりが、目立つようにしたいです。

<表現したいイメージなど>
・信頼感
・ビジネス書っぽい感じ
・ベストセラーのマーケティング関連ビジネス書など、
どこかで見たことがあるような感じの安心感
・カラーの希望などはありません。お任せで。

<利用画像について>
イラスト等素材を使用される場合には、
商用利用可の素材をお願いします。

■その他、デザインを考えるのに必要な情報などありましたら、
お答えしますので、遠慮なく聞いて下さい。
■ 選んだ理由

皆様のレベルが高くて本当に嬉しい限りです。選定したポイントは、2案を出してもらいながら、シンプルで分かりやすく、タイトル周りの文字もメリハリがあり、「強み」「生かす」が強調されており、「人生の転機」も目を引き付けました。「充実した人生」も金色で表現しているところにデザインの秀逸さを感じました。また、ビジネス本という視点からも、青白でシンプルに構成され伝わりやすい表現がベストセラーにも多いので、そこにも共感をしました。一部修正依頼をさせていただいた対応も迅速丁寧で感謝しております。

■ 提案者全員のお礼・コメント

皆様、多くの素晴らしいご提案をいただき感謝しております。本当にありがとうございました。次回の依頼する際におきましてもご協力いただきますようお願いいたします。今後ともどうぞよろしくお願いいたします。

```html
<!DOCTYPE html>
<html lang="ja">
<head>
<meta charset="utf-8">
<title>40代からのあなたの強みを最大限に生かすための3つの視点</title>
<link href="https://fonts.googleapis.com/css2?family=Noto+Sans+JP:wght@500;700;900&display=swap" rel="stylesheet">
<style>
:root{
  --ink:#111;
  --green:#1f9a3c;
  --marker:#f3e14a;
  --orange:#f08a1c;
  --paper:#fff;
  --photo-light:#b8b2a8;
  --photo-dark:#4d4a45;
}
*{margin:0;padding:0;box-sizing:border-box}
html,body{width:751px;height:1200px;overflow:hidden;background:var(--paper)}
.cover{position:relative;width:751px;height:1200px;background:var(--paper);font-family:"Noto Sans JP",sans-serif;color:var(--ink)}
.catch{position:absolute;top:22px;left:0;width:100%;text-align:center;font-weight:900;font-size:34px;letter-spacing:1px}
.catch .hint{color:var(--green);font-size:46px}
.photo{position:absolute;top:112px;left:0;width:751px;height:683px;
  background:linear-gradient(100deg,var(--photo-dark) 0%,#7d776e 35%,var(--photo-light) 70%,#d5d0c7 100%)}
.title-panel{position:absolute;top:150px;left:140px;width:600px;height:570px;background:rgba(255,255,255,.72)}
.title{position:absolute;top:160px;left:150px;font-weight:900;font-size:76px;line-height:82px;letter-spacing:-1px}
.title .line{display:block;white-space:nowrap}
.title .mark{background:linear-gradient(transparent 62%,var(--marker) 62%,var(--marker) 92%,transparent 92%)}
.title .points{display:block;margin-top:6px;font-size:96px;line-height:112px}
.title .points .num{font-size:118px}
.title .points .big{font-size:118px}
.subtitle{position:absolute;top:790px;left:0;width:100%;text-align:center;color:var(--green);font-weight:700;font-size:52px;line-height:60px}
.credo{position:absolute;top:935px;left:28px;font-weight:900;font-size:35px;line-height:50px}
.swoosh{position:absolute;left:20px;top:1060px}
.author{position:absolute;left:440px;top:1045px;font-weight:700}
.author .org{font-size:22px;display:block;margin-left:10px}
.author .role{font-size:22px}
.author .name{font-size:42px;letter-spacing:1px}
.author .by{font-size:22px}
</style>
</head>
<body>
<div class="cover">
  <p class="catch">人生の転機の<span class="hint">ヒント</span>が得られる！</p>
  <div class="photo" role="img" aria-label="夕暮れの高層ビル群を窓辺から見下ろすビジネスマンのシルエット写真"></div>
  <div class="title-panel"></div>
  <h1 class="title">
    <span class="line"><span class="mark">40代からの</span></span>
    <span class="line"><span class="mark">あなたの強みを</span></span>
    <span class="line"><span class="mark">最大限に</span></span>
    <span class="line"><span class="mark">生かすための</span></span>
    <span class="points"><span class="mark"><span class="num">3</span>つの<span class="big">視点</span></span></span>
  </h1>
  <p class="subtitle">ビジネスもプライベートも<br>充実した人生を手に入れる</p>
  <p class="credo">ハンディや持病を抱え<br>ながらも一部上場企業<br>に貢献し、独立・起業<br>したコーチが伝える</p>
  <svg class="swoosh" width="360" height="140" viewBox="0 0 360 140" aria-hidden="true">
    <path d="M300 28 C220 8 60 20 20 60 C-5 90 40 125 150 122 C250 120 330 100 335 70" fill="none" stroke="var(--orange)" stroke-width="7" stroke-linecap="round"/>
  </svg>
  <p class="author">
    <span class="org">M&amp;R 合同会社 代表</span>
    <span class="role">ライフコーチ</span><span class="name">前田芳典</span><span class="by">著</span>
  </p>
</div>
</body>
</html>
```